Tallowmoor Letterheads Design

Hello, we have just upgraded this project for a guaranteed payment.

We are currently going through a re-branding exercise internally. Our logo is attached as a PDF file.

We are happy with our logo but would like to investigate how we can best apply the logo to our letterheads and compliment slips.

We are a quality printing company in England. Despite our name we are very professional and offer a personal service.

Our new website is under construction and here is a link to show you how it looks: http://brackenpress.v4ntor.co.uk

The style must be professional and steer away from "tacky" otherwise it makes our company look very low budget and just a bit silly.

We would like to see elements of creativity though, so please, nothing too boring.

I have attached our new logo, there is an option for use on white or black.

Cheers
Tallowmoor Team

Reason: We have increased the deadline due to an internal delay to things, we now have more time before we need anything to be printed.

Industry/Entity Type

Construction

Requirements
Must have
• IMPORTANT! Please do not tweak or change our logo in any way. A few designs show vast changes in the logo, this is not what we require. Please do not change the logo in any way. Thanks
Nice to have
• Classy but approachable. Elements of "quirky" would be nice to see.
Should not have
• A Tacky feel

```html
<!DOCTYPE html>
<html lang="en">
<head>
<meta charset="utf-8">
<title>Tallowmoor Letterhead</title>
<link href="https://fonts.googleapis.com/css2?family=Montserrat:wght@500;600&display=swap" rel="stylesheet">
<style>
  :root {
    --ink-dark: #102a25;
    --ink-pink: #ee2a8c;
    --paper: #ffffff;
    --brand-text: #16202c;
  }
  html, body {
    margin: 0;
    padding: 0;
    overflow: hidden;
    background: var(--paper);
  }
  .letterhead {
    position: relative;
    width: 930px;
    height: 1200px;
    overflow: hidden;
    font-family: "Montserrat", Arial, sans-serif;
  }
  .droplet-border {
    position: absolute;
    inset: 0;
    background:
      linear-gradient(135deg,
        var(--ink-dark) 0%,
        #3a2a3a 22%,
        var(--ink-pink) 45%,
        #4a2b40 62%,
        var(--ink-dark) 80%,
        #5c2c4c 100%);
  }
  .writing-panel {
    position: absolute;
    left: 114px;
    top: 103px;
    width: 708px;
    height: 973px;
    background: var(--paper);
  }
  .brand-mark {
    position: absolute;
    left: 600px;
    top: 945px;
    width: 200px;
    text-align: center;
  }
  .brand-dot {
    display: block;
    width: 30px;
    height: 30px;
    margin: 0 auto 14px;
    border-radius: 50%;
    background: var(--ink-pink);
  }
  .brand-name {
    display: block;
    font-size: 27px;
    font-weight: 600;
    line-height: 1;
    color: var(--brand-text);
    letter-spacing: -0.2px;
  }
  .brand-tagline {
    display: block;
    margin-top: 8px;
    font-size: 11.5px;
    font-weight: 500;
    color: var(--brand-text);
    letter-spacing: 0.2px;
  }
</style>
</head>
<body>
  <div class="letterhead">
    <div class="droplet-border" role="img" aria-label="Decorative border pattern of overlapping pink, dark green and white ink droplets"></div>
    <div class="writing-panel">
    </div>
    <div class="brand-mark">
      <span class="brand-dot"></span>
      <span class="brand-name">Tallowmoor</span>
      <span class="brand-tagline">Quality Printing</span>
    </div>
  </div>
</body>
</html>
```